Private Investigation Business Card Design

I need a business card for a new private investigation company named Brisk Lens Inquiries. I perform mainly surveillance jobs, vehicle repossessions, document serves etc. The final design should aim for a professional look. The logo has a magnifying glass with stick man arms and legs and is in a running action to show the "BRISK" aspect of the name. If the colour scheme could remain the same as the website www.brisklensinquiries.example.au with silvers,blacks and a couple electric blue highlights.
Industry/Entity Type
Business
Contact Information for Business Card
Morgan Kilbride
Brisk Lens Inquiries
0438276104
PO Box 58, Fernvale NSW 2291
info@brisklensinquiries.example.au
www.brisklensinquiries.example.au
Look and feel
Each slider illustrates characteristics of the customer's brand and the style your logo design should communicate.

```html
<!DOCTYPE html>
<html lang="en">
<head>
<meta charset="utf-8">
<title>Brisk Lens Inquiries – Business Card</title>
<link href="https://fonts.googleapis.com/css2?family=Oswald:wght@600;700&family=EB+Garamond:ital@1&display=swap" rel="stylesheet">
<style>
  :root {
    --backdrop: #eceef0;
    --card: #fbfbfb;
    --ink: #161616;
    --silver: #7d8084;
    --rule: #2a2a2a;
    --shadow: rgba(0, 0, 0, 0.12);
  }
  * { margin: 0; padding: 0; box-sizing: border-box; }
  html, body {
    width: 1200px;
    height: 800px;
    overflow: hidden;
    background: var(--backdrop);
  }
  .canvas {
    width: 1200px;
    height: 800px;
    display: flex;
    align-items: center;
    justify-content: center;
    gap: 60px;
  }
  .card {
    width: 500px;
    height: 286px;
    background: var(--card);
    box-shadow: 0 6px 18px var(--shadow);
    position: relative;
  }
  /* Front side */
  .card-front {
    display: flex;
    align-items: center;
    justify-content: center;
  }
  .brand {
    display: flex;
    align-items: center;
    gap: 18px;
  }
  .brand-name {
    font-family: "Oswald", sans-serif;
    font-weight: 700;
    color: var(--silver);
    text-transform: uppercase;
    line-height: 1;
  }
  .brand-name .brand-main {
    display: block;
    font-size: 72px;
    letter-spacing: 2px;
  }
  .brand-name .brand-sub {
    display: block;
    font-size: 20px;
    letter-spacing: 6px;
    margin-top: 6px;
  }
  .brand-mark {
    width: 34px;
    height: 34px;
    border-radius: 50%;
    background: var(--silver);
    align-self: flex-start;
    margin-top: 4px;
  }
  /* Back side */
  .card-back {
    display: flex;
    align-items: center;
    padding-left: 50px;
  }
  .holder-name {
    font-family: "Oswald", sans-serif;
    font-weight: 700;
    font-size: 40px;
    line-height: 1.02;
    color: var(--ink);
    text-transform: uppercase;
    letter-spacing: 0.5px;
    padding-right: 14px;
    border-right: 1.5px solid var(--rule);
    height: 96px;
    display: flex;
    flex-direction: column;
    justify-content: center;
  }
  .contact-list {
    list-style: none;
    padding-left: 10px;
    font-family: "EB Garamond", serif;
    font-style: italic;
    font-size: 12.5px;
    color: var(--ink);
  }
  .contact-list li {
    display: flex;
    align-items: center;
    gap: 7px;
    height: 22px;
  }
  .contact-list svg {
    width: 11px;
    height: 11px;
    flex: none;
    fill: var(--ink);
  }
</style>
</head>
<body>
<main class="canvas">
  <section class="card card-front" aria-label="Card front">
    <div class="brand">
      <div class="brand-name">
        <span class="brand-main">Brisk</span>
        <span class="brand-sub">Lens Inquiries</span>
      </div>
      <span class="brand-mark" aria-hidden="true"></span>
    </div>
  </section>

  <section class="card card-back" aria-label="Card back">
    <h1 class="holder-name"><span>Morgan</span><span>Kilbride</span></h1>
    <ul class="contact-list">
      <li>
        <svg viewBox="0 0 24 24" aria-hidden="true"><path d="M6.6 10.8a15.1 15.1 0 0 0 6.6 6.6l2.2-2.2a1 1 0 0 1 1-.25 11.4 11.4 0 0 0 3.6.57 1 1 0 0 1 1 1V20a1 1 0 0 1-1 1A17 17 0 0 1 3 4a1 1 0 0 1 1-1h3.5a1 1 0 0 1 1 1c0 1.25.2 2.45.57 3.57a1 1 0 0 1-.25 1z"/></svg>
        0438276104
      </li>
      <li>
        <svg viewBox="0 0 24 24" aria-hidden="true"><path d="M3 5h18v14H3zm2 2v.5l7 5 7-5V7zm0 3v7h14v-7l-7 5z"/></svg>
        info@brisklensinquiries.example.au
      </li>
      <li>
        <svg viewBox="0 0 24 24" aria-hidden="true"><circle cx="12" cy="12" r="10"/></svg>
        www.brisklensinquiries.example.au
      </li>
      <li>
        <svg viewBox="0 0 24 24" aria-hidden="true"><path d="M12 2a7 7 0 0 0-7 7c0 5.2 7 13 7 13s7-7.8 7-13a7 7 0 0 0-7-7zm0 9.5A2.5 2.5 0 1 1 12 6.5a2.5 2.5 0 0 1 0 5z"/></svg>
        PO Box 58, Fernvale NSW 2291
      </li>
    </ul>
  </section>
</main>
</body>
</html>
```